Veltrix Hand Sanitiser Spray Product Range for International Markets

Veltrix is a new Healthcare business launching a full product range of Anti-bacterial Hand Sanitiser Spray bottles in various sizes. We have a new logo which we believe differentiates us from the competition: Veltrix - Care That Stays With You
The Product Range will comprise two distinct product solution types:
- Anti-bacterial Hand Sanitisers - Alcohol based
- Anti-bacterial Hand Sanitisers - Sensitive Non Alcohol based
Bottle sizes will comprise a range containing:
100ml, 250ml, 500ml, 1ltr, 5ltr, 10ltr
Some bottles will have Pump Sprays
The Product labelling will be attractive front packaging label combined with strong product attributes and usage indicator cues.
As a Healthcare brand our logo design is light Green. We believe that this should be combined with blues and greens balanced to create contrast and strong stand-out on-shelf.
A review of competitor brands will show some similar colour cues, however as a Healthcare brand, the colour cues Green and White are synonymous with the sector. Many existing brands are very pragmatic in their label design. i.e. #it does what is says on the tin approach#. Our brand will need strong stand-out and strong aesthetic appeal too, since it will often be left in public view and around the home and office and therefore should look as attractive as possible. There will be other brand variants in the future and thought should be given to this too - with use of colour cues.
For Competitor indicators check-out the brands on Shopvale - Birch Lane, Dermalux and others....Thank-you!

Target Market(s)

First: Female 25 - 65
Second: Male 25 - 65

Contact Information for Business Card

Greg T. Hollis
CEO
Veltrix Healthcare International
'Care That Stays With You'
www.VeltrixHealthcare.example
E. gthollis@veltrixhealthcare.example
T. +44 7700 900312
T. +44 118 496051

Font styles to use
Sans Serif

Colors
34a7d7
33b8a4
add136
fbee3e
b768aa

```html
<!DOCTYPE html>
<html lang="en">
<head>
<meta charset="utf-8">
<title>Veltrix Hand Sanitiser – Product Board</title>
<link href="https://fonts.googleapis.com/css2?family=Montserrat:wght@800;900&family=Oswald:wght@600&family=Open+Sans:wght@400;600;700&display=swap" rel="stylesheet">
<style>
  :root {
    --board-bg: #f2f2f2;
    --sky: #34a7d7;
    --teal: #1fa88e;
    --aqua: #33b8a4;
    --leaf: #5cbd5e;
    --lime: #add136;
    --label-white: #ffffff;
    --ink: #3a3a3a;
    --photo-light: #e6e6e6;
    --photo-dark: #8a8a8a;
  }
  * { margin: 0; padding: 0; box-sizing: border-box; }
  html, body { width: 1200px; height: 913px; overflow: hidden; background: var(--board-bg); }
  .board { position: relative; width: 1200px; height: 913px; background: var(--board-bg); }
  .board svg { position: absolute; left: 0; top: 0; }
  .headline {
    position: absolute; left: 58px; top: 722px; color: #fff;
    font-family: "Montserrat", sans-serif; font-weight: 900; line-height: 1;
    white-space: nowrap;
  }
  .headline .big { font-size: 58px; letter-spacing: 0; }
  .headline .small { font-size: 27px; font-weight: 800; letter-spacing: 1px; margin-top: 8px; margin-left: 27px; }
  .label-type { font-family: "Open Sans", sans-serif; }
  .brand-name { font-family: "Open Sans", sans-serif; font-weight: 400; }
  .product-name { font-family: "Oswald", sans-serif; font-weight: 600; }
</style>
</head>
<body>
<main class="board">
  <svg width="1200" height="913" viewBox="0 0 1200 913">
    <defs>
      <linearGradient id="mosaic" x1="0" y1="0" x2="1" y2="1">
        <stop offset="0" stop-color="var(--sky)"/>
        <stop offset="0.45" stop-color="var(--aqua)"/>
        <stop offset="0.75" stop-color="var(--leaf)"/>
        <stop offset="1" stop-color="var(--lime)"/>
      </linearGradient>
      <linearGradient id="photoTone" x1="0" y1="0" x2="1" y2="0">
        <stop offset="0" stop-color="var(--photo-dark)"/>
        <stop offset="1" stop-color="var(--photo-light)"/>
      </linearGradient>
      <linearGradient id="labelMosaic" x1="0" y1="0" x2="1" y2="1">
        <stop offset="0" stop-color="var(--aqua)"/>
        <stop offset="0.5" stop-color="var(--leaf)"/>
        <stop offset="1" stop-color="var(--lime)"/>
      </linearGradient>
      <clipPath id="labelClip"><rect x="740" y="298" width="260" height="470" rx="8"/></clipPath>
    </defs>

    <polygon class="banner-mosaic" role="img" aria-label="Blue and green triangle mosaic pattern"
      points="0,0 85,0 585,640 440,913 0,913" fill="url(#mosaic)"/>
    <polygon class="photo-frame" points="0,160 412,410 0,665" fill="#8fd19b"/>
    <polygon class="photo-area" role="img" aria-label="Black and white photo of a parent's hand holding a baby's hand"
      points="0,172 392,410 0,652" fill="url(#photoTone)"/>

    <g class="product-label" clip-path="url(#labelClip)">
      <rect x="740" y="298" width="260" height="470" fill="var(--label-white)"/>
      <polygon class="label-mosaic-top" role="img" aria-label="Green and teal triangle mosaic pattern"
        points="740,298 1000,298 1000,398 870,468 740,398" fill="url(#labelMosaic)"/>
      <polygon class="label-mosaic-bottom" role="img" aria-label="Green and teal triangle mosaic pattern"
        points="740,768 1000,768 1000,640 870,740 740,740" fill="url(#labelMosaic)"/>

      <rect class="logo-frame" x="812" y="326" width="130" height="106" fill="none" stroke="#fff" stroke-width="1.2"/>
      <text class="brand-name" x="871" y="390" text-anchor="middle" font-size="36" fill="#fff">Veltrix</text>
      <text class="label-type" x="871" y="411" text-anchor="middle" font-size="8" fill="#fff">Care That Stays With You</text>

      <line x1="776" y1="504" x2="803" y2="504" stroke="var(--leaf)" stroke-width="2"/>
      <line x1="938" y1="504" x2="965" y2="504" stroke="var(--leaf)" stroke-width="2"/>
      <text class="label-type" x="870" y="509" text-anchor="middle" font-size="12.5" font-weight="600" fill="var(--leaf)" letter-spacing="1">ANTI-BACTERIAL</text>

      <rect class="product-band" x="740" y="519" width="260" height="37" fill="var(--teal)"/>
      <text class="product-name" x="869" y="548" text-anchor="middle" font-size="27" fill="#fff">HAND SANITIZER</text>

      <g class="attribute-icons" fill="var(--leaf)" stroke="#fff">
        <circle cx="794" cy="587" r="16" stroke-width="2"/>
        <circle cx="839" cy="587" r="16" stroke-width="2"/>
        <circle cx="887" cy="587" r="16" stroke-width="2"/>
        <circle cx="934" cy="587" r="16" stroke-width="2"/>
        <path d="M787 592 q7 -14 14 0 M794 580 v8" fill="none" stroke-width="2"/>
        <path d="M835 578 h8 M837 578 v6 l-5 10 h14 l-5 -10 v-6" fill="none" stroke-width="2"/>
        <path d="M880 594 q0 -14 14 -14 q0 14 -14 14 z" fill="none" stroke-width="2"/>
        <circle cx="934" cy="587" r="6" fill="none" stroke-width="2"/>
      </g>
      <g class="label-type" font-size="6.5" font-weight="700" fill="var(--ink)" text-anchor="middle">
        <text x="794" y="614">Skin</text><text x="794" y="622">Friendly</text>
        <text x="839" y="614">80% Alcohol</text><text x="839" y="622">Content</text>
        <text x="887" y="614">Bio-Based</text>
        <text x="934" y="614">Kills 99.99%</text><text x="934" y="622">Germs &amp; Bacteria</text>
      </g>

      <g class="feature-list label-type" font-size="8" font-weight="700" fill="var(--ink)">
        <path d="M782 657 l3 3 l5 -6 M782 673 l3 3 l5 -6 M782 689 l3 3 l5 -6" fill="none" stroke="var(--ink)" stroke-width="1.5"/>
        <text x="796" y="662">Ethyl Alcohol Antiseptic</text>
        <text x="796" y="678">Surgical/Medical Grade</text>
        <text x="796" y="694">Fragrance Free</text>
      </g>

      <path class="shield" d="M942 636 l35 13 v38 q0 25 -35 42 q-35 -17 -35 -42 v-38 z" fill="#d9f1f6" stroke="var(--aqua)" stroke-width="3"/>
      <path d="M936 657 h12 v14 h14 v12 h-14 v14 h-12 v-14 h-14 v-12 h14 z" fill="none" stroke="#fff" stroke-width="2.5"/>
      <rect role="img" aria-label="Hand illustration inside the shield" x="936" y="663" width="12" height="30" rx="5" fill="#e9b99a"/>

      <text class="label-type" x="940" y="748" text-anchor="middle" font-size="15" font-weight="700" fill="#fff">500ml</text>
    </g>
  </svg>

  <div class="headline">
    <div class="big">KILLS 99.9%</div>
    <div class="small">GERMS &amp; BACTERIA</div>
  </div>
</main>
</body>
</html>
```